KTV Lanternfall

I need a graphic package design for our new bodybuilding sports supplement. The artwork should be clean and useable for many formats. examples or great usage are www.ferrovigorlab.example, www.quartzpulse.example and http://www.belwinnutrition.example/ as examples. I am adding our logo for your reference. The name Lanternfall is because it will help make "Big Guns" as a catch phrase, the product line will have other supplements such as creatine and protein powders and the artwork should be useable on all products. You can see our website for ideas at www.kestovalife.example
Updates

Hi everyone, There are some nice entries coming in. I do wonder if some of you are reading the brief as a few labels don't even highlight the product, KTV is the company, Lanternfall is the Product. Thanks Tam

Industry/Entity Type

Supplement

```html
<!DOCTYPE html>
<html lang="en">
<head>
<meta charset="utf-8">
<title>KTV Lanternfall Label</title>
<link rel="stylesheet" href="https://fonts.googleapis.com/css2?family=Exo+2:wght@400;700&display=swap">
<style>
  :root {
    --stage: #e4e4e4;
    --label-green-deep: #2f9a12;
    --label-green: #58c21e;
    --label-green-light: #8fdc2a;
    --flame-yellow: #d9ec3c;
    --flame-green: #6fcf22;
    --text-white: #ffffff;
    --text-soft: #eaf7d8;
  }
  html, body {
    margin: 0;
    padding: 0;
    overflow: hidden;
  }
  body {
    width: 1200px;
    height: 1143px;
    background: var(--stage);
    position: relative;
    font-family: "Exo 2", sans-serif;
  }
  .label {
    position: absolute;
    left: 150px;
    top: 262px;
    width: 900px;
    height: 620px;
    overflow: hidden;
    background: linear-gradient(180deg, var(--label-green-deep) 0%, var(--label-green) 45%, var(--label-green-light) 100%);
  }
  .label__flames {
    position: absolute;
    left: 0;
    right: 0;
    bottom: 0;
    height: 300px;
    background: linear-gradient(180deg, rgba(111, 207, 34, 0) 0%, var(--flame-green) 35%, var(--flame-yellow) 100%);
  }
  .brand {
    position: absolute;
    left: 0;
    right: 0;
    text-align: center;
    color: var(--text-white);
    font-weight: 700;
    margin: 0;
    white-space: nowrap;
  }
  .brand__mark {
    top: 20px;
    font-size: 270px;
    line-height: 1;
    letter-spacing: 4px;
  }
  .brand__product {
    top: 335px;
    font-size: 92px;
    line-height: 1;
    letter-spacing: 2px;
  }
  .brand__company {
    top: 442px;
    font-size: 24px;
    font-weight: 400;
    line-height: 1;
    letter-spacing: 12px;
    padding-left: 12px;
    color: var(--text-soft);
  }
  .volume {
    position: absolute;
    left: 0;
    right: 0;
    bottom: 44px;
    margin: 0;
    text-align: center;
    color: var(--text-white);
    font-weight: 700;
    font-size: 46px;
    line-height: 1;
    white-space: nowrap;
  }
</style>
</head>
<body>
  <section class="label">
    <div class="label__flames" role="img" aria-label="Yellow-green flame pattern across the lower label"></div>
    <p class="brand brand__mark">KTV</p>
    <p class="brand brand__product">LANTERNFALL</p>
    <p class="brand brand__company">KESTOVA LIFE-SCIENCE</p>
    <p class="volume">140 FL OZ (500 mL)</p>
  </section>
</body>
</html>
```